I need a better looking dashboard for my web application

I have a very table heavy web page that I would like to add a design touch to it. I have the logo and primary colors picked out, I just need some help in adding visual appeal the page. I would also like to add a couple of button to the page as shortcuts. Every spot that has a + sign could have a button added. I would also like to add another graph (the data will be in the uploaded files. Please feel free to ask any questions :-)

```html
<!DOCTYPE html>
<html lang="en">
<head>
<meta charset="utf-8">
<title>CoverDesk Dashboard</title>
<link rel="stylesheet" href="https://fonts.googleapis.com/css2?family=Nunito:wght@400;600;700&display=swap">
<style>
:root{
  --page:#dde4eb;
  --main:#eef3f8;
  --white:#ffffff;
  --teal:#29afd4;
  --teal-soft:#d8eef6;
  --purple:#6a4cad;
  --purple-light:#7a5eb8;
  --lavender:#f1eef8;
  --ink:#222;
  --muted:#555;
  --line:#e8ebf0;
  --dark:#231f20;
  --bar-1:#1b0e4a;
  --bar-2:#3d1fa0;
  --bar-3:#6a3fb5;
  --bar-4:#7b5fba;
}
*{box-sizing:border-box;margin:0;padding:0}
html,body{width:1200px;height:797px;overflow:hidden}
body{background:var(--page);font-family:"Nunito",sans-serif;color:var(--ink);position:relative}
.app{position:absolute;left:31px;top:34px;width:1118px;height:729px;border-radius:31px;overflow:hidden;background:var(--main)}
.sidebar{position:absolute;left:0;top:0;width:225px;height:100%;background:var(--white)}
.brand{position:absolute;left:38px;top:26px;display:flex;align-items:center;gap:7px;font-size:22px;font-weight:600;color:var(--purple)}
.brand-mark{width:14px;height:14px;border-radius:50%;background:var(--teal)}
.nav-item{position:absolute;left:0;width:205px;height:32px;display:flex;align-items:center;gap:8px;padding-left:37px;font-size:12px;color:#444}
.nav-item.active{top:80px;background:var(--teal);color:var(--white);border-radius:0 16px 16px 0}
.nav-item.cal{top:120px}
.nav-item svg{width:11px;height:11px}
.search{position:absolute;left:270px;top:24px;width:204px;height:29px;background:var(--white);border-radius:15px;display:flex;align-items:center;justify-content:space-between;padding:0 12px 0 17px;font-size:8.5px;color:#aab}
.topnav{position:absolute;top:31px;font-size:10.6px;color:#333}
.user{position:absolute;left:924px;top:26px;display:flex;gap:6px;align-items:center}
.avatar{width:26px;height:26px;border-radius:50%;background:var(--purple);color:var(--white);font-size:11px;display:flex;align-items:center;justify-content:center}
.user-mail{font-size:9.5px;color:var(--purple)}
.user-out{font-size:8px;color:#555;margin-top:2px}
.divider{position:absolute;left:225px;right:0;top:75px;height:1px;background:#e4e9f0}
.tab{position:absolute;top:94px;height:29px;border-radius:15px;background:var(--teal-soft);color:var(--teal);font-size:10.6px;display:flex;align-items:center;justify-content:center;white-space:nowrap;overflow:hidden}
.tab.active{background:var(--purple);color:var(--white)}
.openings{position:absolute;left:270px;top:139px;width:816px;border-collapse:collapse;table-layout:fixed;background:var(--white);font-size:8.6px;color:#444}
.openings th{height:33px;background:var(--purple);color:var(--white);font-weight:400;text-align:left;font-size:8.8px}
.openings th.alt{background:var(--purple-light)}
.openings td{height:37.4px;border-bottom:1px solid var(--line)}
.openings tr:last-child td{border-bottom:none}
.openings td.alt{background:var(--lavender)}
.c-act{padding-left:18px}.c-cat{padding-left:14px}.c-staff{padding-left:29px}.c-stat{padding-left:24px}.c-sum{padding-left:35px}.c-loc{padding-left:28px}.c-time{padding-left:34px}
.acts{display:flex;gap:10px;padding-left:4px}
.acts svg{width:8px;height:8px}
.add{display:flex;align-items:center;gap:6px}
.add svg{width:8px;height:8px}
.card{position:absolute;top:458px;width:194px;height:193px;background:var(--white);border-radius:3px;overflow:hidden}
.card-head{height:33px;background:var(--teal);color:var(--white);font-size:12px;font-weight:600;display:flex;align-items:center;justify-content:center}
.stat-row{position:absolute;left:21px;width:152px;display:flex;justify-content:space-between;font-size:10px;color:#111}
.stat-row span:last-child{width:24px;color:#333}
.day{position:absolute;left:11px;top:43px;font-size:10px;color:#333}
.bar{position:absolute;left:11px;top:68px;width:172px;height:12px;display:flex}
.legend-item{position:absolute;left:11px;display:flex;align-items:center;gap:7px;font-size:10px;color:#333}
.sw{width:9px;height:9px;display:inline-block}
.pie{position:absolute;left:50px;top:53px;width:94px;height:94px}
.pie-legend{position:absolute;top:157px;left:15px;display:flex;gap:14px;font-size:10px;color:#333}
.pie-legend span{display:flex;align-items:center;gap:6px}
.btn{position:absolute;top:673px;height:31px;background:var(--teal);color:var(--white);font-size:10.5px;font-weight:600;display:flex;align-items:center;justify-content:center}
</style>
</head>
<body>
<div class="app">
  <aside class="sidebar">
    <div class="brand"><span class="brand-mark"></span>CoverDesk</div>
    <div class="nav-item active">
      <svg viewBox="0 0 12 12" fill="#fff"><path d="M6 1 0.5 6h1.7v5h3V8h1.6v3h3V6h1.7z"/></svg>Dashboard</div>
    <div class="nav-item cal">
      <svg viewBox="0 0 12 12" fill="none" stroke="#666" stroke-width="1"><rect x="1" y="2" width="10" height="9"/><path d="M1 4.5h10M3.5 1v2M8.5 1v2M3 6.5h1M5.5 6.5h1M8 6.5h1M3 8.5h1M5.5 8.5h1M8 8.5h1"/></svg>Calendar</div>
  </aside>

  <div class="search">Tap to search
    <svg width="9" height="9" viewBox="0 0 10 10" fill="none" stroke="#29afd4" stroke-width="1.4"><circle cx="4.2" cy="4.2" r="3"/><path d="M6.4 6.4 9 9"/></svg></div>
  <span class="topnav" style="left:518px">Home</span>
  <span class="topnav" style="left:587px">Demo Outbox</span>
  <span class="topnav" style="left:695px">Location Admin</span>
  <span class="topnav" style="left:813px">Regular Staff</span>
  <div class="user"><div class="avatar">D</div><div><div class="user-mail">ops.lead@coverdesk.test</div><div class="user-out">Logout</div></div></div>
  <div class="divider"></div>

  <div class="tab active" style="left:270px;width:129px">Managed Openings</div>
  <div class="tab" style="left:410px;width:185px">Regular Staff Leave Requests</div>
  <div class="tab" style="left:605px;width:128px">Location Overview</div>
  <div class="tab" style="left:743px;width:151px">Pending Profile Images</div>
  <div class="tab" style="left:903px;width:132px">My Leave Requests</div>
  <div class="tab" style="left:1044px;width:90px;justify-content:flex-start;padding-left:18px">Substitude</div>

  <table class="openings">
    <colgroup><col style="width:88px"><col style="width:106px"><col style="width:120px"><col style="width:95px"><col style="width:159px"><col style="width:77px"><col style="width:171px"></colgroup>
    <thead><tr>
      <th class="c-act"><span class="add"><svg viewBox="0 0 8 8"><rect width="8" height="8" rx="1" fill="#fff"/><path d="M4 2v4M2 4h4" stroke="#6a4cad" stroke-width="1.2"/></svg>Add New</span></th>
      <th class="c-cat alt">Category</th><th class="c-staff">Regular Staff</th><th class="c-stat alt">Status</th><th class="c-sum">Summary</th><th class="c-loc alt">Location</th><th class="c-time">Time Slots</th>
    </tr></thead>
    <tbody>
      <tr><td class="c-act"><span class="acts"><svg viewBox="0 0 8 8" fill="none" stroke="#555" stroke-width=".8"><rect x=".5" y="1.5" width="6" height="6"/><path d="M3 5l.3-1.3L7 0.5l.5.5L4.3 4.7z"/></svg><svg viewBox="0 0 8 8" fill="none" stroke="#555" stroke-width=".8"><path d="M1 2h6M3 2V1h2v1M1.8 2l.5 5.5h3.4L6.2 2M3.5 3.5v3M4.5 3.5v3"/></svg></span></td><td class="c-cat alt">Food Service</td><td class="c-staff">Extra Duty</td><td class="c-stat alt">Assigned</td><td class="c-sum">Immediate Need!</td><td class="c-loc alt">LJE</td><td class="c-time">12/30-01/01 (2h 30m)</td></tr>
      <tr><td class="c-act"><span class="acts"><svg viewBox="0 0 8 8" fill="none" stroke="#555" stroke-width=".8"><rect x=".5" y="1.5" width="6" height="6"/><path d="M3 5l.3-1.3L7 0.5l.5.5L4.3 4.7z"/></svg><svg viewBox="0 0 8 8" fill="none" stroke="#555" stroke-width=".8"><path d="M1 2h6M3 2V1h2v1M1.8 2l.5 5.5h3.4L6.2 2M3.5 3.5v3M4.5 3.5v3"/></svg></span></td><td class="c-cat alt">Teacher</td><td class="c-staff">Nora Wells</td><td class="c-stat alt">Available</td><td class="c-sum">Immediate Need!</td><td class="c-loc alt">WDMS</td><td class="c-time">12/30-01/01 (2h 30m)</td></tr>
      <tr><td class="c-act"><span class="acts"><svg viewBox="0 0 8 8" fill="none" stroke="#555" stroke-width=".8"><rect x=".5" y="1.5" width="6" height="6"/><path d="M3 5l.3-1.3L7 0.5l.5.5L4.3 4.7z"/></svg><svg viewBox="0 0 8 8" fill="none" stroke="#555" stroke-width=".8"><path d="M1 2h6M3 2V1h2v1M1.8 2l.5 5.5h3.4L6.2 2M3.5 3.5v3M4.5 3.5v3"/></svg></span></td><td class="c-cat alt">Bus Driver</td><td class="c-staff">Extra Duty</td><td class="c-stat alt">Available</td><td class="c-sum">Immediate Need!</td><td class="c-loc alt">WDMS</td><td class="c-time">12/30-01/01 (2h 30m)</td></tr>
      <tr><td class="c-act"><span class="acts"><svg viewBox="0 0 8 8" fill="none" stroke="#555" stroke-width=".8"><rect x=".5" y="1.5" width="6" height="6"/><path d="M3 5l.3-1.3L7 0.5l.5.5L4.3 4.7z"/></svg><svg viewBox="0 0 8 8" fill="none" stroke="#555" stroke-width=".8"><path d="M1 2h6M3 2V1h2v1M1.8 2l.5 5.5h3.4L6.2 2M3.5 3.5v3M4.5 3.5v3"/></svg></span></td><td class="c-cat alt">Custodian</td><td class="c-staff">Extra Duty</td><td class="c-stat alt">Available</td><td class="c-sum">Seeking Sub for couns..</td><td class="c-loc alt">FMS</td><td class="c-time">12/30-01/01 (2h 30m)</td></tr>
      <tr><td class="c-act"><span class="acts"><svg viewBox="0 0 8 8" fill="none" stroke="#555" stroke-width=".8"><rect x=".5" y="1.5" width="6" height="6"/><path d="M3 5l.3-1.3L7 0.5l.5.5L4.3 4.7z"/></svg><svg viewBox="0 0 8 8" fill="none" stroke="#555" stroke-width=".8"><path d="M1 2h6M3 2V1h2v1M1.8 2l.5 5.5h3.4L6.2 2M3.5 3.5v3M4.5 3.5v3"/></svg></span></td><td class="c-cat alt">Teacher’s Aide</td><td class="c-staff">Extra Duty</td><td class="c-stat alt">Available</td><td class="c-sum">Seeking Sub for IT</td><td class="c-loc alt">FMS</td><td class="c-time">12/30-01/01 (2h 30m)</td></tr>
      <tr><td class="c-act"><span class="acts"><svg viewBox="0 0 8 8" fill="none" stroke="#555" stroke-width=".8"><rect x=".5" y="1.5" width="6" height="6"/><path d="M3 5l.3-1.3L7 0.5l.5.5L4.3 4.7z"/></svg><svg viewBox="0 0 8 8" fill="none" stroke="#555" stroke-width=".8"><path d="M1 2h6M3 2V1h2v1M1.8 2l.5 5.5h3.4L6.2 2M3.5 3.5v3M4.5 3.5v3"/></svg></span></td><td class="c-cat alt">Food Service</td><td class="c-staff">Grace Rowan</td><td class="c-stat alt">Available</td><td class="c-sum">Seeking Sub for SS</td><td class="c-loc alt">FMS</td><td class="c-time">12/30-01/01 (2h 30m)</td></tr>
      <tr><td class="c-act"><span class="acts"><svg viewBox="0 0 8 8" fill="none" stroke="#555" stroke-width=".8"><rect x=".5" y="1.5" width="6" height="6"/><path d="M3 5l.3-1.3L7 0.5l.5.5L4.3 4.7z"/></svg><svg viewBox="0 0 8 8" fill="none" stroke="#555" stroke-width=".8"><path d="M1 2h6M3 2V1h2v1M1.8 2l.5 5.5h3.4L6.2 2M3.5 3.5v3M4.5 3.5v3"/></svg></span></td><td class="c-cat alt">Teacher's Aide</td><td class="c-staff">Alan Brooks</td><td class="c-stat alt">Available</td><td class="c-sum">Substitude Needed.</td><td class="c-loc alt">LJE</td><td class="c-time">12/30-01/01 (2h 30m)</td></tr>
    </tbody>
  </table>

  <section class="card" style="left:270px">
    <div class="card-head">MONTHLY SUMMARY</div>
    <div class="stat-row" style="top:45px"><span>Total Jobs</span><span>45</span></div>
    <div class="stat-row" style="top:67px"><span>Filled Jobs</span><span>Data</span></div>
    <div class="stat-row" style="top:89px"><span>No Sub Needed</span><span>Data</span></div>
  </section>

  <section class="card" style="left:485px">
    <div class="card-head">TODAYS SUMMARY</div>
    <div class="day">Jan 22</div>
    <div class="bar"><span style="width:11px;background:var(--bar-1)"></span><span style="width:66px;background:var(--bar-2)"></span><span style="width:57px;background:var(--bar-3)"></span><span style="width:38px;background:var(--bar-4)"></span></div>
    <div class="legend-item" style="top:96px"><span class="sw" style="background:var(--bar-1)"></span>Unfilled</div>
    <div class="legend-item" style="top:121px"><span class="sw" style="background:var(--bar-2)"></span>Filled</div>
    <div class="legend-item" style="top:146px"><span class="sw" style="background:var(--bar-3)"></span>No Sub Needed</div>
    <div class="legend-item" style="top:170px"><span class="sw" style="background:var(--bar-4)"></span>Total</div>
  </section>

  <section class="card" style="left:700px">
    <div class="card-head">MONTHLY FILL RATE</div>
    <svg class="pie" viewBox="-47 -47 94 94">
      <g stroke="#fff" stroke-width="1.5">
        <path d="M0 0 L0 -47 A47 47 0 0 1 41.19 22.64 Z" fill="#29afd4"/>
        <path d="M0 0 L41.19 22.64 A47 47 0 0 1 -46.63 5.89 Z" fill="#6a4cad"/>
        <path d="M0 0 L-46.63 5.89 A47 47 0 0 1 0 -47 Z" fill="#231f20"/>
      </g>
      <g fill="#fff" font-family="Nunito, sans-serif" font-size="7" font-weight="700" text-anchor="middle">
        <text x="24" y="-13">33%</text>
        <text x="-5" y="23">40%</text>
        <text x="-18" y="-24">27%</text>
      </g>
    </svg>
    <div class="pie-legend">
      <span><i class="sw" style="background:var(--teal)"></i>Open</span>
      <span><i class="sw" style="background:var(--purple)"></i>Filled</span>
      <span><i class="sw" style="background:var(--dark)"></i>No Sub</span>
    </div>
  </section>

  <div class="btn" style="left:270px;width:108px">Create Vacancy</div>
  <div class="btn" style="left:394px;width:88px">Approve 3</div>
  <div class="btn" style="left:498px;width:108px">Create Absence</div>
  <div class="btn" style="left:621px;width:87px">Approve 8</div>
</div>
</body>
</html>
```